Webdesign für Ingenieurbüro
Zielgruppe
Ingenieurbüro Varnotek GmbH
Leistungen:
Siedlungswasserwirtschaft
Straßen- und Ingenieurbau
Hochwasserschutz / Wasserbau
Pegelanlagen
Komplexerschließungen
Koordinierung nach BaustellV
Landschaftsbau
Zielgruppe ist die Öffentliche Hand
Aufgabenstellung
Leistungsbereiche und Stellenangebote (zZt. 3 Stück) sollen zu gleichen Teilen im Fokus stehen. Call to action zum Berweberformular ist nötig.
Zu beachten wäre, dass das Unternehmen für öffentliche Auftraggeber arbeitet. Die Seite sollte klar strukturiert und seriös wirken.
Der Login-Bereich soll in den Hintergrund treten, eventuell über dem footer.
Logo aus dem Cover - siehe anbei übernehmen

```html
<!DOCTYPE html>
<html lang="de">
<head>
<meta charset="utf-8">
<title>Ingenieurbüro Varnotek GmbH</title>
<link href="https://fonts.googleapis.com/css2?family=Lato:wght@400;700;900&display=swap" rel="stylesheet">
<style>
:root{
  --navy:#0b3e93;
  --navy-dark:#0c2a6b;
  --brand:#0b4ea2;
  --sky:#0a9be0;
  --pale:#eaf4fb;
  --text:#1d2a3a;
  --white:#ffffff;
  --line:#dfe6ee;
}
*{box-sizing:border-box;margin:0;padding:0}
html,body{width:1200px;height:2700px;overflow:hidden}
body{position:relative;font-family:'Lato',sans-serif;color:var(--text);background:var(--white)}
.abs{position:absolute}

/* header */
.hero{left:0;top:0;width:1200px;height:525px;background:linear-gradient(100deg,#eaf4fb 0%,#cfe2f0 40%,#9eb0c0 75%,#6f7f8e 100%)}
.topbar{left:0;top:0;width:1200px;height:53px;background:var(--navy)}
.mainnav{right:170px;top:0;height:53px;display:flex;gap:44px;align-items:center}
.mainnav a{color:var(--white);text-decoration:none;font-size:14px}
.brandmark{left:118px;top:12px;width:230px;height:190px;background:rgba(255,255,255,.92);border-radius:50%;display:flex;flex-direction:column;align-items:center;justify-content:center;gap:8px}
.brandmark .sq{width:44px;height:44px;background:var(--brand)}
.brandmark .name{font-size:15px;font-weight:700;color:var(--brand);text-align:center;line-height:1.25}
.hero-title{left:117px;top:312px;font-size:40px;font-weight:900;color:var(--brand);line-height:1.1;letter-spacing:-1px}
.hero-sub{left:120px;top:422px;width:470px;height:30px;background:var(--sky);color:var(--white);font-size:17px;padding:4px 12px}
.quickform{left:955px;top:141px;width:245px;height:307px;background:var(--sky);padding:27px 21px 0 28px}
.quickform h3{color:var(--white);font-size:14.5px;font-weight:700;line-height:1.2;margin-bottom:16px}
.quickform .field{background:var(--white);height:28px;margin-bottom:6px;font-size:10px;color:#777;padding:8px 11px}
.quickform .field.area{height:62px}
.quickform .send{background:var(--navy);color:var(--white);height:28px;font-size:12px;text-align:center;line-height:28px;margin-top:8px}

/* welcome */
.welcome{left:0;top:525px;width:1200px;height:283px;background:var(--pale);border-bottom:1px solid var(--line)}
h2{font-weight:400;color:var(--brand);font-size:29px}
.welcome h2{position:absolute;left:120px;top:50px}
.welcome p{position:absolute;top:102px;width:330px;font-size:12.5px;line-height:22.5px}
.welcome .c1{left:120px}.welcome .c2{left:507px}
.photo-frame{left:855px;top:50px;width:220px;height:170px;background:var(--white);padding:9px;transform:rotate(-4deg);box-shadow:0 4px 14px rgba(0,0,0,.2)}
.photo-frame div{width:100%;height:100%;background:linear-gradient(180deg,#b9d3ea 0%,#e8eef3 45%,#8a8f96 100%)}

/* services */
.services-title{left:0;top:858px;width:1200px;text-align:center}
.card{width:210px;height:158px;background:var(--white);box-shadow:0 2px 10px rgba(0,0,0,.08);text-align:center}
.card svg{position:absolute;left:75px;top:26px}
.card .rule{position:absolute;left:22px;right:22px;top:110px;height:1px;background:var(--line)}
.card .label{position:absolute;left:0;right:0;top:118px;height:36px;display:flex;align-items:center;justify-content:center;font-size:13.5px;line-height:16px;color:#333}
.card.active{background:var(--sky)}
.card.active .label{color:var(--white);font-weight:700}
.card.active .rule{background:rgba(255,255,255,.35)}

/* jobs */
.jobs-photo{left:0;top:1347px;width:600px;height:362px;background:radial-gradient(circle at 22% 20%,#f2c9a0 0%,#b08c7a 30%,#5a5560 70%,#3b3c45 100%)}
.jobs{left:600px;top:1347px;width:600px;height:362px;background:var(--sky);color:var(--white);padding:72px 42px}
.jobs h3{font-size:20px;font-weight:700;margin-bottom:20px}
.jobs .lead{font-size:12.5px;font-weight:700;margin-bottom:20px}
.jobs ul{list-style:none}
.jobs li{font-size:12.5px;line-height:22.5px;padding-left:17px;position:relative}
.jobs li::before{content:"›";position:absolute;left:0;top:-1px;font-size:16px}
.apply{display:inline-block;margin-top:25px;border:2px solid var(--white);padding:7px 24px;font-size:12.5px;font-weight:700}

/* projects */
.projects-title{left:0;top:1755px;width:1200px;text-align:center}
.project{width:300px;height:205px;top:1823px}
.project .img{height:175px}
.project .cap{height:30px;background:var(--navy);color:var(--white);font-size:13px;font-weight:700;padding:7px 13px}
.arrow{top:1903px}

/* certificates */
.certs{left:0;top:2086px;width:1200px;height:360px;background:var(--pale);border-top:1px solid var(--line)}
.certs h2{position:absolute;left:120px;top:115px}
.certs .intro{position:absolute;left:120px;top:155px;width:360px;font-size:12px;line-height:21px}
.pager{top:39px;width:27px;height:30px;background:var(--navy);display:flex;align-items:center;justify-content:center}
.pager.prev{left:1025px;background:var(--sky)}
.pager.next{left:1053px}
.cert{width:266px;height:108px;background:var(--white);box-shadow:0 2px 8px rgba(0,0,0,.07);padding:18px 20px;font-size:11px;line-height:18px}
.cert b{display:block;color:var(--brand);font-size:11.5px;margin-bottom:2px}

/* login */
.login{left:0;top:2446px;width:1200px;height:122px;background:linear-gradient(90deg,#0b4ea2 0%,#0d63c0 60%,#1a88d6 100%)}
.login h3{position:absolute;left:336px;top:22px;color:var(--white);font-size:18px;font-weight:700}
.login .inp{position:absolute;top:49px;width:265px;height:36px;background:var(--white);font-size:12px;padding:10px 12px}
.login .btn{position:absolute;left:902px;top:49px;width:178px;height:36px;background:var(--navy);color:var(--white);font-size:13px;font-weight:700;text-align:center;line-height:36px}
.login .forgot{position:absolute;right:120px;top:94px;color:var(--white);font-size:11.5px;font-weight:700}

/* footer */
.footer{left:0;top:2568px;width:1200px;height:132px;background:var(--navy-dark);color:var(--white);font-size:10.5px;line-height:18px}
.footer .addr{position:absolute;left:120px;top:42px}
.footer .addr b{font-size:12.5px}
.footer .contact{position:absolute;left:515px;top:40px}
.footer .sep{position:absolute;top:45px;width:1px;height:50px;background:rgba(255,255,255,.3)}
.socials{position:absolute;right:120px;top:60px;display:flex;gap:20px}
.socials span{width:15px;height:15px;border-radius:50%;background:#cfe0f5}
</style>
</head>
<body>

<header>
  <div class="abs hero" role="img" aria-label="Foto einer Autobahn mit Leitplanke und Lärmschutzwand"></div>
  <div class="abs topbar"></div>
  <nav class="abs mainnav">
    <a href="#">Home</a><a href="#">Stellenangebote</a><a href="#">Leistungen</a><a href="#">Unternehmen</a><a href="#">Projekte</a><a href="#">Kontakt</a>
  </nav>
  <div class="abs brandmark"><span class="sq"></span><span class="name">Ingenieurbüro<br>Varnotek GmbH</span></div>
  <h1 class="abs hero-title">Über 25 Jahre Ingenieurbüro<br>VARNOTEK GmbH</h1>
  <div class="abs hero-sub">Ingenieurleistungen aus Chemnitz-Rabenstein seit 1991</div>
  <form class="abs quickform">
    <h3>Excepteur sint occaecat cupidatat non proident</h3>
    <div class="field">Name</div>
    <div class="field">Email</div>
    <div class="field">Telefon</div>
    <div class="field area">Kommentare</div>
    <div class="send">SENDEN</div>
  </form>
</header>

<section class="abs welcome">
  <h2>Herzlich willkommen</h2>
  <p class="c1">Willkommen bei der Ingenieurbüro VARNOTEK GmbH, einem mittelständischen Unternehmen, welches 1991 gegründet wurde. Wir sind ein zuverlässiger Partner für fachgerechte Beratung, Planung und Bauüberwachung von Maßnahmen des Tief-, Wasser- und Straßenbaues.</p>
  <p class="c2">Hierfür sind 18 hochqualifizierte und engagierte Ingenieure und technische Mitarbeiter verantwortlich. Moderne Kommunikationstechnik und Spezialsoftware, sowie die Kreativität der Mitarbeiter sind ein Garant für effektive Lösungen.</p>
  <div class="abs photo-frame"><div role="img" aria-label="Foto des Bürogebäudes mit Parkplatz"></div></div>
</section>

<h2 class="abs services-title">Leistungen</h2>
<div class="abs card" style="left:120px;top:930px">
  <svg width="60" height="60" viewBox="0 0 60 60" fill="none" stroke="#0a9be0" stroke-width="2.2"><path d="M24 6 C14 22 10 30 10 38 a14 14 0 0 0 20 12"/><circle cx="34" cy="32" r="9"/><circle cx="34" cy="32" r="3.5"/></svg>
  <div class="rule"></div><div class="label">Siedlungswasser-<br>wirtschaft</div>
</div>
<div class="abs card active" style="left:370px;top:930px">
  <svg width="60" height="60" viewBox="0 0 60 60" fill="none" stroke="#fff" stroke-width="2"><circle cx="30" cy="30" r="30" fill="rgba(255,255,255,.18)" stroke="none"/><path d="M16 32 a14 14 0 0 1 28 0 z"/><path d="M13 32h34"/><path d="M22 36 a8 8 0 0 0 16 0"/></svg>
  <div class="rule"></div><div class="label">Straßen- und<br>Ingenieurbau</div>
</div>
<div class="abs card" style="left:619px;top:930px">
  <svg width="60" height="60" viewBox="0 0 60 60" fill="none" stroke="#0b4ea2" stroke-width="2.2"><path d="M10 30 L28 14 L46 30 M15 26v16h26V26"/><path d="M25 42v-9h6v9"/><path d="M8 48c6-3 10 3 16 0s10 3 16 0 8 3 12 0" stroke="#0a9be0"/></svg>
  <div class="rule"></div><div class="label">Hochwasserschutz /<br>Wasserbau</div>
</div>
<div class="abs card" style="left:869px;top:930px">
  <svg width="60" height="60" viewBox="0 0 60 60" fill="none" stroke-width="5"><path d="M12 44 A20 20 0 1 1 48 44" stroke="#0b4ea2"/><path d="M30 40 L38 24" stroke="#0a9be0" stroke-width="3"/></svg>
  <div class="rule"></div><div class="label">Pegelanlagen</div>
</div>
<div class="abs card" style="left:245px;top:1125px">
  <svg width="60" height="60" viewBox="0 0 60 60" fill="none" stroke="#0b4ea2" stroke-width="1.8"><rect x="12" y="10" width="36" height="36"/><path d="M12 10l36 36M48 10L12 46M30 10v36M12 28h36"/><path d="M10 52h40" stroke="#0a9be0"/></svg>
  <div class="rule"></div><div class="label">Komplexerschließungen</div>
</div>
<div class="abs card" style="left:495px;top:1125px">
  <svg width="60" height="60" viewBox="0 0 60 60" fill="none" stroke="#0b4ea2" stroke-width="1.8"><circle cx="30" cy="30" r="16" stroke="#0a9be0"/><rect x="8" y="8" width="9" height="9"/><rect x="43" y="8" width="9" height="9"/><circle cx="12" cy="47" r="5"/><circle cx="48" cy="47" r="5"/></svg>
  <div class="rule"></div><div class="label">Koordinierung nach<br>BaustellV</div>
</div>
<div class="abs card" style="left:744px;top:1125px">
  <svg width="60" height="60" viewBox="0 0 60 60" fill="none" stroke="#0b4ea2" stroke-width="2"><path d="M30 8v6M30 14L20 50M30 14l10 36M23 36h14"/><path d="M10 40 L14 18 L18 40z" fill="#0a9be0" stroke="none"/><path d="M44 40 L48 20 L52 40z" fill="#0a9be0" stroke="none"/></svg>
  <div class="rule"></div><div class="label">Landschaftsbau</div>
</div>

<div class="abs jobs-photo" role="img" aria-label="Foto eines gelben Schutzhelms auf Solarmodulen im Gegenlicht"></div>
<section class="abs jobs">
  <h3>Stellenangebote</h3>
  <p class="lead">Wir haben aktuell Stellenangebote aus den folgenden Bereichen:</p>
  <ul><li>Hydrologie</li><li>Wasserwirtschaft</li><li>Verkehrsanlagen</li></ul>
  <span class="apply">›&nbsp; Jetzt bewerben</span>
</section>

<h2 class="abs projects-title">Projekte</h2>
<svg class="abs arrow" style="left:72px" width="24" height="36" viewBox="0 0 24 36" fill="none" stroke="#0a9be0" stroke-width="2.5"><path d="M20 2 L4 18 L20 34"/></svg>
<div class="abs project" style="left:120px"><div class="img" role="img" aria-label="Baustelle Kanalbau mit Bauzaun vor Wohnhaus" style="background:linear-gradient(180deg,#cfd8de,#7b8a72 60%,#6f6b64)"></div><div class="cap">›&nbsp; Siedlungswasserwirtschaft</div></div>
<div class="abs project" style="left:450px"><div class="img" role="img" aria-label="Straßenbaustelle mit Asphaltfertiger und Bauarbeitern" style="background:linear-gradient(180deg,#e2e7ec,#8f9590 55%,#4d5054)"></div><div class="cap">›&nbsp; Straßen- und Ingenieurbau</div></div>
<div class="abs project" style="left:779px"><div class="img" role="img" aria-label="Grüner Deich an einem Bach vor Gewerbegebäuden" style="background:linear-gradient(180deg,#7ea4d6,#bccbd8 45%,#5f7d3c 65%,#3f5a2a)"></div><div class="cap">›&nbsp; Hochwasserschutz / Wasserbau</div></div>
<svg class="abs arrow" style="left:1104px" width="24" height="36" viewBox="0 0 24 36" fill="none" stroke="#0a9be0" stroke-width="2.5"><path d="M4 2 L20 18 L4 34"/></svg>

<section class="abs certs">
  <div class="abs pager prev"><svg width="8" height="12" viewBox="0 0 8 12" fill="none" stroke="#fff" stroke-width="1.6"><path d="M6 1L1 6l5 5"/></svg></div>
  <div class="abs pager next"><svg width="8" height="12" viewBox="0 0 8 12" fill="none" stroke="#fff" stroke-width="1.6"><path d="M2 1l5 5-5 5"/></svg></div>
  <h2>Zertifikate</h2>
  <p class="intro">Die Mitarbeiter der Varnotek GmbH nehmen regelmäßig an Fortbildungen und Qualifizierungen teil.<br>Hier erhalten Sie einen Überblick der absolvierten Seminare seit 1992. Gern senden wir Ihnen auf Anfrage das gewünschte bzw. detaillierte Dokument zu.</p>
  <div class="abs cert" style="left:529px;top:86px;padding-left:34px"><b>17.05.-21.05.2010</b>Qualifizierung zum Sicherheits- und Gesundheitsschutz-Koordinator gemäß Anlagen B &amp; C zur RAB 30 in Neuss</div>
  <div class="abs cert" style="left:811px;top:84px"><b>28.01.2010</b>Fachseminar über den Schutz hydraulischer Systeme vor Luftansammlungen, Unterdruck/Vakuum und dynamischen Druckänderungen/Druckstoß in Chemnitz</div>
  <div class="abs cert" style="left:529px;top:209px;padding-top:30px"><b>20.11.2009</b>Seminar Vertragsgestaltung und Abrechnung nach der neuen HOAI in Dresden</div>
  <div class="abs cert" style="left:811px;top:207px"><b>07.10.2009</b>Fortbildung mit ausgewählten Themen aus Straßenplanung und Straßenentwurf in Dresden</div>
</section>

<section class="abs login">
  <svg class="abs" style="left:120px;top:14px" width="110" height="96" viewBox="0 0 110 96" fill="none" stroke="#fff" stroke-width="2.5"><circle cx="27" cy="24" r="20"/><path d="M3 90 V66 a22 22 0 0 1 44 0 V82 z"/><rect x="56" y="42" width="44" height="36" rx="4" stroke="#6fc3f2" transform="rotate(-12 78 60)"/><path d="M64 42 v-10 a14 14 0 0 1 28 -4" stroke="#6fc3f2"/></svg>
  <h3>Interner Bereich</h3>
  <div class="inp" style="left:336px">Kundennummer</div>
  <div class="inp" style="left:620px">Passwort</div>
  <div class="btn">LOGIN</div>
  <div class="forgot">Passwort vergessen?</div>
</section>

<footer class="abs footer">
  <div class="addr"><b>Ingenieurbüro Varnotek GmbH</b><br>Talsperrenweg 48<br>09123 Chemnitz</div>
  <div class="sep" style="left:395px"></div>
  <div class="contact">Tel.&nbsp;&nbsp; 0371 / 40682-0<br>Fax:&nbsp; 0371 / 40682-43<br>Email : ingenieurbuero@varnotek.de</div>
  <div class="sep" style="left:804px"></div>
  <div class="socials"><span aria-label="Soziales Netzwerk"></span><span aria-label="Soziales Netzwerk"></span><span aria-label="Videoplattform"></span><span aria-label="Kurznachrichtendienst"></span><span aria-label="Berufsnetzwerk"></span></div>
</footer>

</body>
</html>
```